Ventrox Corporate General Presentation

Ventrox is a leading player in ICT (Information Communication Technology) cooling, we need a design for our corporate general presentation.

Attached is a reference of content

Our logo main color is industrial blue, our technology is green (energy saving).

existing website: www.ven-trox.example www.ven-trox.example.uk

Hi, this is a package with USD 620 for PPT and 290 for 5 web pages, plus 100 each for number 2 and 3 position in the tender Added Wednesday, December 30, 2015

Target Market(s)

Global

Industry/Entity Type

Communication

Number of Pages Required

5+ page

Font styles to use
Serif
Sans Serif

Colors
0255a3
3176b5
0293ce
33a6d7
9bcb3c

```html
<!DOCTYPE html>
<html lang="en">
<head>
<meta charset="utf-8">
<title>Ventrox – ICT Cooling</title>
<link href="https://fonts.googleapis.com/css2?family=Roboto:ital,wght@0,300;0,400;0,500;0,700;1,400&display=swap" rel="stylesheet">
<style>
:root{
  --blue:#0255a3;
  --blue-2:#3176b5;
  --blue-3:#0293ce;
  --blue-4:#33a6d7;
  --green:#9bcb3c;
  --green-light:#b2d862;
  --ink:#222;
  --text:#555;
  --muted:#888;
  --line:#dcdcdc;
  --panel:#f1f1f1;
  --dark:#3b3b3b;
  --darker:#2d2d2d;
  --white:#fff;
}
*{box-sizing:border-box;margin:0;padding:0}
html,body{width:1200px;height:3822px;overflow:hidden;background:var(--white)}
body{font-family:"Roboto",Arial,sans-serif;color:var(--text);position:relative}
.block{position:absolute}
ul{list-style:none}

/* header */
.topbar{left:498px;top:0;width:643px;height:30px;background:#ececec;display:flex;align-items:center;font-size:11px;color:#666;padding-left:12px;gap:18px}
.topbar .dots{display:flex;gap:12px}
.topbar .dots span{width:8px;height:8px;border-radius:50%;background:#999;display:block}
.topbar .contact{display:flex;align-items:center;gap:6px;margin-left:14px}
.brand{left:191px;top:48px;font-size:36px;font-weight:700;color:var(--blue);letter-spacing:1px}
.nav{left:490px;top:94px;width:651px;display:flex;justify-content:space-between;font-size:11.5px;font-weight:500;color:#333;text-transform:uppercase}

/* hero */
.hero{left:59px;top:168px;width:1082px;height:529px;background:linear-gradient(100deg,#36475a 0%,#5d7a94 30%,#cfdbe6 55%,#eef3f7 100%)}
.hero-copy{left:613px;top:276px;width:460px;color:#111}
.hero-copy .kicker{font-size:26px;font-weight:400;margin-left:44px}
.hero-copy h1{font-size:40px;font-weight:400;line-height:1;letter-spacing:.5px;margin-top:-10px}
.hero-copy h1 .cap{font-size:84px;font-weight:500;line-height:.8;vertical-align:-4px}
.hero-copy p{font-size:13px;line-height:19px;margin-top:16px;color:#222;width:440px}

/* features */
.features{left:59px;top:697px;width:1082px;height:186px;background:var(--green);display:flex;padding:42px 0 0 60px;gap:62px}
.feature{width:290px;color:var(--white)}
.feature h3{font-size:19px;font-weight:400;display:flex;align-items:center;gap:12px}
.feature p{font-size:11px;line-height:15px;margin-top:10px}

/* quote */
.quote{left:59px;top:914px;width:1082px;height:120px;background:var(--panel);border-left:4px solid var(--blue-2)}
.quote .avatar{position:absolute;left:34px;top:16px;width:62px;height:62px;border-radius:50%;background:linear-gradient(#b7c3cf,#7b8a99)}
.quote p{position:absolute;left:144px;top:28px;width:910px;font-size:12.5px;font-style:italic;line-height:18px;color:#777}
.quote .by{position:absolute;right:40px;top:84px;font-size:11.5px;font-style:italic;color:#555}

/* about */
.h2{font-size:21px;font-weight:500;color:var(--ink)}
.about-photo{left:59px;top:1164px;width:342px;height:388px;background:linear-gradient(160deg,#eef2f5 0%,#c8d2dc 55%,#8b97a3 100%)}
.about-text{left:424px;top:1172px;width:340px;font-size:12.5px;line-height:18px;color:#666}
.about-text h3{font-size:14px;font-weight:500;line-height:20px;color:#222;text-transform:uppercase;margin-bottom:16px}
.about-text p{margin-bottom:14px}
.news{left:800px;top:1172px;width:341px}
.news li{display:flex;gap:12px;font-size:11px;line-height:15px;color:#666;margin-bottom:16px;min-height:30px}
.news .tick{flex:none;width:13px;height:13px;background:var(--green);display:flex;align-items:center;justify-content:center;margin-top:1px}

/* products */
.products{left:59px;top:1601px;width:1082px;height:584px;background:linear-gradient(180deg,#2b2b2b 0%,#161616 60%,#0e0e0e 100%)}
.products .eyebrow{position:absolute;top:68px;width:100%;text-align:center;font-size:15px;color:#ddd}
.products h2{position:absolute;top:94px;width:100%;text-align:center;font-size:27px;font-weight:500;color:var(--white)}
.card{position:absolute;top:201px;width:312px;color:#ddd}
.card .shot{height:202px}
.card h3{font-size:15px;font-weight:500;color:var(--white);margin-top:24px}
.card p{font-size:11px;line-height:15px;margin-top:6px;color:#bbb}
.card .more{font-size:11px;color:var(--green);margin-top:6px;display:block}

/* why choose */
.why{left:0;top:2232px;width:1200px;text-align:center}
.why .eyebrow{font-size:15px;color:#333;font-weight:500}
.why h2{font-size:29px;font-weight:500;color:#111;margin-top:4px}
.accordion{left:243px;top:2356px;width:712px}
.acc-head{height:39px;display:flex;align-items:center;justify-content:center;font-size:14px;border:1px solid var(--line);color:#333;margin-top:10px}
.acc-head.open{background:var(--green);color:var(--white);border-color:var(--green);margin-top:0}
.acc-body{text-align:center;font-size:14px;line-height:22px;color:#666;padding:14px 0 22px}

/* milestone */
.milestone{left:59px;top:2698px;width:1082px;height:383px;background:var(--green);color:var(--white)}
.milestone .eyebrow{position:absolute;left:38px;top:72px;font-size:12px;font-weight:500}
.milestone h2{position:absolute;left:38px;top:96px;font-size:27px;font-weight:500}
.milestone p{position:absolute;left:38px;top:148px;width:500px;font-size:11px;line-height:17px}
.milestone .cta{position:absolute;left:38px;top:276px;width:120px;height:36px;background:#111;color:var(--white);font-size:11px;font-weight:500;display:flex;align-items:center;justify-content:center}
.stat{position:absolute;width:240px;text-align:center}
.stat strong{display:block;font-size:34px;font-weight:700;line-height:1;margin-top:6px}
.stat span{display:block;font-size:15px;font-weight:500;margin-top:6px}

/* partners */
.partners{left:59px;top:3102px;width:1082px;height:140px}
.partners .arrow{position:absolute;top:30px}
.partner{position:absolute;top:52px;width:170px;text-align:center;font-size:20px;font-weight:500;color:#555}

/* footer */
.footer{left:0;top:3360px;width:1200px;height:393px;background:var(--dark)}
.info-band{left:59px;top:3303px;width:1082px;height:110px;display:flex}
.info-band .cell{flex:1;background:var(--green);color:var(--white);display:flex;gap:18px;padding:30px 0 0 34px}
.info-band .cell.mid{background:var(--green-light)}
.info-band h4{font-size:11px;font-weight:700;text-transform:uppercase}
.info-band p{font-size:10.5px;line-height:14px;margin-top:4px}
.foot-brand{left:140px;top:3552px;font-size:40px;font-weight:500;color:#9a9a9a;letter-spacing:2px}
.foot-title{font-size:14px;font-weight:500;color:var(--white);text-transform:uppercase;padding-bottom:8px;border-bottom:1px solid #555;margin-bottom:16px}
.services{left:447px;top:3460px;width:330px}
.services ul{display:grid;grid-template-columns:1fr 1fr;row-gap:12px;font-size:11px;color:#ccc}
.services li::before{content:"›";margin-right:8px;color:#aaa}
.newsletter{left:835px;top:3460px;width:306px;font-size:11px;color:#ccc;line-height:15px}
.newsletter form{display:flex;margin-top:14px}
.newsletter .field{flex:1;height:32px;background:var(--white);color:#444;font-size:11px;display:flex;align-items:center;padding-left:10px}
.newsletter .send{width:78px;height:32px;background:var(--green);color:var(--white);font-size:11px;font-weight:500;display:flex;align-items:center;justify-content:center}
.newsletter h5{font-size:11px;font-weight:500;color:var(--white);margin-top:22px;text-transform:uppercase}
.newsletter .dots{display:flex;gap:22px;margin-top:14px}
.newsletter .dots span{width:9px;height:9px;border-radius:50%;background:#bbb;display:block}
.copyright{left:0;top:3753px;width:1200px;height:69px;background:var(--darker);text-align:center;font-size:10.5px;line-height:17px;color:#999;padding-top:16px}
</style>
</head>
<body>

<!-- header -->
<div class="block topbar">
  <span>Some Lorem Ipsum</span><span>EN</span>
  <span class="dots"><span></span><span></span><span></span><span></span><span></span></span>
  <span class="contact"><svg width="12" height="9" viewBox="0 0 12 9"><rect x=".5" y=".5" width="11" height="8" fill="none" stroke="#666"/><path d="M.5 .5 6 5 11.5 .5" fill="none" stroke="#666"/></svg>info@ven-trox.example.uk</span>
  <span class="contact"><svg width="10" height="10" viewBox="0 0 10 10"><path d="M2 0 4 2.5 3 4a6 6 0 0 0 3 3l1.5-1L10 8 8.5 10C4 9.5.5 6 0 1.5Z" fill="#666"/></svg>+44 (0)100 555 0142</span>
</div>
<div class="block brand">VENTROX</div>
<nav class="block nav">
  <span>Home</span><span>About Us</span><span>Cooling Solutions ⌄</span><span>News</span><span>Factory</span><span>Refences ⌄</span><span>Contact Us</span>
</nav>

<!-- hero -->
<div class="block hero" role="img" aria-label="Photo of a smiling businessman in a suit with colleagues meeting in a bright office behind him"></div>
<div class="block hero-copy">
  <div class="kicker">Stay Responsive</div>
  <h1><span class="cap">A</span>DVANCED COOLING</h1>
  <p>Ut enim ad minim veniam, quis nostrud exercitation ullamco laboris nisi ut aliquip ex ea commodo consequat. Excepteur sint occaecat cupidatat non proident ...</p>
</div>

<!-- features -->
<section class="block features">
  <div class="feature">
    <h3><svg width="20" height="22" viewBox="0 0 20 22" fill="#fff"><ellipse cx="10" cy="4" rx="9" ry="3.5"/><path d="M1 7c0 2 4 3.5 9 3.5S19 9 19 7v4c0 2-4 3.5-9 3.5S1 13 1 11Z"/><path d="M1 14.5c0 2 4 3.5 9 3.5s9-1.5 9-3.5v3.5c0 2-4 3.5-9 3.5S1 20 1 18Z"/></svg>Data centre cooling</h3>
    <p>Lorem ipsum dolor sit amet, consectetur adipisicing elit, sed do eiusmod tempor incididunt ut labore et dolore magna aliqua.</p>
  </div>
  <div class="feature">
    <h3><svg width="20" height="20" viewBox="0 0 10 10"><path d="M2 0 4 2.5 3 4a6 6 0 0 0 3 3l1.5-1L10 8 8.5 10C4 9.5.5 6 0 1.5Z" fill="#fff"/></svg>Telecom cooling</h3>
    <p>Lorem ipsum dolor sit amet, consectetur adipisicing elit, sed do eiusmod tempor incididunt ut labore et dolore magna aliqua.</p>
  </div>
  <div class="feature">
    <h3><svg width="22" height="22" viewBox="0 0 22 22"><rect width="22" height="22" rx="2" fill="#fff"/><path d="M9 4h4v5h5v4h-5v5H9v-5H4V9h5Z" fill="#9bcb3c"/></svg>Medical equipment cooling</h3>
    <p>Lorem ipsum dolor sit amet, consectetur adipisicing elit, sed do eiusmod tempor incididunt ut labore et dolore magna aliqua.</p>
  </div>
</section>

<!-- testimonial -->
<section class="block quote">
  <div class="avatar" role="img" aria-label="Portrait of the quoted client"></div>
  <p>Duis aute irure dolor in reprehenderit in voluptate velit esse cillum dolore eu fugiat nulla pariatur incididunt ut labore et dolore magna aliqua. Ut enim ad minim veniam ...</p>
  <div class="by">by Daniel Ashford</div>
</section>

<!-- about -->
<h2 class="block h2" style="left:59px;top:1096px">About Our Company</h2>
<h2 class="block h2" style="left:800px;top:1096px">Hale &amp; Brandt</h2>
<div class="block about-photo" role="img" aria-label="Photo of a senior businessman in a white shirt and tie sitting at a desk with a laptop"></div>
<div class="block about-text">
  <h3>Be who you are and say what you feel, because those who mind don't matter, and those who matter don't mind.</h3>
  <p>Hello, I'm a UI/UX Designer &amp; Front End Developer from Dhaka, Bangladesh. I hold a master degree of Web Design from the Halden University.</p>
  <p>I currently work at Corvane Labs, where I spend most of my time crafting and working on awesome projects. Lorem ipsum dolor sit amet consectetuer Integer eleifend Cura bitur id ut. Quisque Aenean ut pede id elit ligula est mollis sapien magna. Urna turpis quis sagittis at ac Sed augue habitant tortor elit. Dolor Quisque et elit aliquam vitae habitant.</p>
</div>
<ul class="block news">
  <li><span class="tick"><svg width="9" height="9" viewBox="0 0 10 10"><path d="M1 5h8M5 1v8" stroke="#fff" stroke-width="2"/></svg></span>Low Vitamin D Levels Linked to Weight Gain in Older Women</li>
  <li><span class="tick"><svg width="9" height="9" viewBox="0 0 10 10"><path d="M1 5h8M5 1v8" stroke="#fff" stroke-width="2"/></svg></span>Secondhand Smoke Linked to Raised Diabetes Risk</li>
  <li><span class="tick"><svg width="9" height="9" viewBox="0 0 10 10"><path d="M1 5h8M5 1v8" stroke="#fff" stroke-width="2"/></svg></span>Discovery of 'Master Molecule' Could Improve Stem Cell...</li>
  <li><span class="tick"><svg width="9" height="9" viewBox="0 0 10 10"><path d="M1 5h8M5 1v8" stroke="#fff" stroke-width="2"/></svg></span>Low Vitamin D Levels Linked to Weight Gain in Older Women</li>
  <li><span class="tick"><svg width="9" height="9" viewBox="0 0 10 10"><path d="M1 5h8M5 1v8" stroke="#fff" stroke-width="2"/></svg></span>Low Vitamin D Levels Linked to Weight Gain in Older Women</li>
  <li><span class="tick"><svg width="9" height="9" viewBox="0 0 10 10"><path d="M1 5h8M5 1v8" stroke="#fff" stroke-width="2"/></svg></span>Low Vitamin D Levels Linked to Weight Gain in Older Women</li>
</ul>

<!-- insurance products -->
<section class="block products" role="img" aria-label="Dark background photo of a city street with buildings">
  <div class="eyebrow">WE'VE GOT YOU COVERED</div>
  <h2>OUR INSURANCE PRODUCT</h2>
  <article class="card" style="left:61px">
    <div class="shot" role="img" aria-label="Photo of hands sheltering a paper cut-out family" style="background:linear-gradient(160deg,#8aa3b8,#c9b29a 60%,#8a6a4e)"></div>
    <h3>LIFE INSURANCE</h3>
    <p>Master cleanse selvage 3 wolf moon retro. Hella post-ironic before they sold out pitchfork gastropub dreamcatcher. Flannel collar, kale...</p>
    <span class="more">Read more ........</span>
  </article>
  <article class="card" style="left:388px">
    <div class="shot" role="img" aria-label="Photo of hands around a chalk-drawn house on a blackboard" style="background:linear-gradient(160deg,#5a5f63,#3a3e42 60%,#7a7f84)"></div>
    <h3>HOME INSURANCE</h3>
    <p>Master cleanse selvage 3 wolf moon retro. Hella post-ironic before they sold out pitchfork gastropub dreamcatcher. Flannel collar, kale...</p>
    <span class="more">Read more ........</span>
  </article>
  <article class="card" style="left:712px">
    <div class="shot" role="img" aria-label="Photo of a smiling woman on the phone in a car" style="background:linear-gradient(160deg,#d8dde2,#9aa4ad 60%,#565d63)"></div>
    <h3>AUTO INSURANCE</h3>
    <p>Master cleanse selvage 3 wolf moon retro. Hella post-ironic before they sold out pitchfork gastropub dreamcatcher. Flannel collar, kale...</p>
    <span class="more">Read more ........</span>
  </article>
</section>

<!-- why choose -->
<div class="block why">
  <div class="eyebrow">PRODUCT LINE STRATEGY LEADERSHIP</div>
  <h2>WHY CHOOSE VENTROX</h2>
</div>
<div class="block accordion">
  <div class="acc-head open">DEMAND</div>
  <ul class="acc-body">
    <li>Acquire competions customers</li>
    <li>Increase renewal rates</li>
    <li>Increase upsell rates</li>
    <li>Build a reputation fo vitue</li>
    <li>Increase market penetration</li>
  </ul>
  <div class="acc-head">BRANDS</div>
  <div class="acc-head">COMPETITIVE POSITIONING</div>
</div>

<!-- milestone -->
<section class="block milestone">
  <div class="eyebrow">SUCESSFUL MILESTONE AREA</div>
  <h2>THE IMPORTANCE OF BEING COVERED</h2>
  <p>We have been providing stability and reliability to our clients since 1850 to help them live lives with confidence, to give them peace of mind, and enable them to realize their dreams for loved ones and their legacy. We have been providing stability and reliability to our clients to help them live their lives with confidence, to give them peace of mind, and enable them dreams for their loved ones and their legacy.</p>
  <div class="cta">TALK TO US</div>
  <div class="stat" style="left:561px;top:66px">
    <svg width="28" height="26" viewBox="0 0 28 26" fill="#fff"><path d="M1 12A13 11 0 0 1 27 12Z"/><path d="M13 12h2v10a3 3 0 0 1-6 0h2a1 1 0 0 0 2 0Z"/></svg>
    <strong>7968</strong><span>INSURANCE POLICIES</span>
  </div>
  <div class="stat" style="left:810px;top:66px">
    <svg width="26" height="26" viewBox="0 0 26 26"><circle cx="13" cy="13" r="12" fill="#fff"/><path d="M6 8c3 0 4 2 3 4s2 3 1 6M16 4c0 3 2 3 4 4M18 16c1 2 0 4-2 5" stroke="#9bcb3c" stroke-width="2" fill="none"/></svg>
    <strong>7968</strong><span>INSURANCE POLICIES</span>
  </div>
  <div class="stat" style="left:561px;top:214px">
    <svg width="26" height="26" viewBox="0 0 26 26" fill="none" stroke="#fff" stroke-width="4"><path d="M4 4 22 22M22 4 4 22"/></svg>
    <strong>7968</strong><span>INSURANCE POLICIES</span>
  </div>
  <div class="stat" style="left:810px;top:214px">
    <svg width="24" height="26" viewBox="0 0 24 26" fill="#fff"><path d="M9 0h6v10h5l-8 9-8-9h5Z"/><rect x="2" y="22" width="20" height="4"/></svg>
    <strong>7968</strong><span>INSURANCE POLICIES</span>
  </div>
</section>

<!-- partners -->
<section class="block partners">
  <svg class="arrow" style="left:36px" width="22" height="70" viewBox="0 0 22 70"><path d="M20 2 2 35l18 33" fill="none" stroke="#ccc" stroke-width="2"/></svg>
  <svg class="arrow" style="left:1024px" width="22" height="70" viewBox="0 0 22 70"><path d="M2 2l18 33L2 68" fill="none" stroke="#ccc" stroke-width="2"/></svg>
  <div class="partner" style="left:144px">Kestrel Telecom</div>
  <div class="partner" style="left:346px">Orbilink</div>
  <div class="partner" style="left:553px">Veralta</div>
  <div class="partner" style="left:762px">Vocanet</div>
</section>

<!-- footer -->
<footer class="block footer"></footer>
<div class="block info-band">
  <div class="cell">
    <svg width="16" height="22" viewBox="0 0 16 22"><path d="M8 0a8 8 0 0 1 8 8c0 6-8 14-8 14S0 14 0 8a8 8 0 0 1 8-8Z" fill="#fff"/><circle cx="8" cy="8" r="3" fill="#9bcb3c"/></svg>
    <div><h4>Hospital Address</h4><p>22, Harbour Lane, Cedar Point<br>Northvale - 204</p></div>
  </div>
  <div class="cell mid">
    <svg width="20" height="20" viewBox="0 0 10 10"><path d="M2 0 4 2.5 3 4a6 6 0 0 0 3 3l1.5-1L10 8 8.5 10C4 9.5.5 6 0 1.5Z" fill="#fff"/></svg>
    <div><h4>Emergency ( 24x7 )</h4><p>(+1)555 010 274<br>Call Us Now 24/7 Customer Support</p></div>
  </div>
  <div class="cell">
    <svg width="22" height="16" viewBox="0 0 22 16"><rect x="1" y="1" width="20" height="14" fill="none" stroke="#fff" stroke-width="2"/><path d="M1 1l10 8 10-8" fill="none" stroke="#fff" stroke-width="2"/></svg>
    <div><h4>Hospital Address</h4><p>care@ven-trox.example<br>help@ven-trox.example</p></div>
  </div>
</div>
<div class="block foot-brand">VENTROX</div>
<div class="block services">
  <div class="foot-title">Our Services</div>
  <ul>
    <li>Births</li><li>Dental</li>
    <li>Pulmonary</li><li>Nuclear magnetic</li>
    <li>Cardiology</li><li>Pregnancy</li>
    <li>Neurology</li><li>For disabled</li>
    <li>Traumatology</li><li>X-ray</li>
    <li>Neurology</li><li>Prosthesis</li>
  </ul>
</div>
<div class="block newsletter">
  <div class="foot-title">Newsletter</div>
  <p>Accusamus et iusto odio dignissimos ducimus blanditiis praesentium quas molestias excepturi.</p>
  <form><div class="field">Email Address</div><div class="send">SEND</div></form>
  <h5>Stay Connected</h5>
  <div class="dots"><span></span><span></span><span></span><span></span></div>
</div>
<div class="block copyright">Copyright © 2015 Ventrox. All Rights Reserved | Sitemap<br>Website by : northwind studio</div>

</body>
</html>
```